Renewal of the Ferolanza SA Website

Ferolanza SA is a metal construction company active in industrial piping, boilermaking and metal framing. We would like to renew our site.

This website must be ready to work with Wordpress.

The site will contain the following pages: Home, skills, presentation, contact.

The site must reflect the field of the metal construction sector. It must be clear and easily understandable. The objective is not to win mandates with but to present the company and its capabilities.

I have inserted the pages of our old presentations, to describe our sector but we do not want to reuse these elements, we are waiting for your creativity to surprise us. In the 2nd phase we will complete with new images if necessary and texts

Target Market(s)

International companies in the food, chemical and pharmaceutical sectors

Industry/Entity Type

Alimentaire, pharma, chimie

Number of Pages Required

4 page

Font styles to use
Sans Serif

Colors
0054AA
0677BA
7BADD7
CADEEF
E8F1F8

Requirements
Must have
• It must contain at least the requested pages, images of illustrations, places for descriptions
Should not have
• Elements that appear or disappear, too flash,

```html
<!DOCTYPE html>
<html lang="fr">
<head>
<meta charset="utf-8">
<title>Ferolanza SA</title>
<link href="https://fonts.googleapis.com/css2?family=Poppins:wght@400;500;600;700&display=swap" rel="stylesheet">
<style>
:root{
  --blue:#0054AA;--blue2:#0677BA;--blue3:#7BADD7;--blue4:#CADEEF;--blue5:#E8F1F8;
  --ink:#1b1d22;--text:#55595f;--light:#f3f4f6;--dark:#0d0e10;--white:#fff;--star:#f2b51c;
}
*{box-sizing:border-box;margin:0;padding:0}
html,body{width:1200px;height:4020px;overflow:hidden}
body{font-family:'Poppins',sans-serif;color:var(--ink);background:var(--white);position:relative}
p{font-size:13px;line-height:1.7;color:var(--text)}
.btn{display:inline-block;background:var(--blue);color:#fff;font-size:12px;font-weight:500;padding:10px 20px;border-radius:2px}
.btn-white{background:#fff;color:var(--blue)}
/* header */
.site-header{position:absolute;top:0;left:0;width:1200px;height:70px;background:#fff;display:flex;align-items:center;justify-content:space-between;padding:0 140px 0 140px;z-index:3}
.brand{display:flex;align-items:center;gap:10px;font-weight:700;font-size:22px;color:var(--ink);letter-spacing:1px}
.brand-dot{width:30px;height:30px;border-radius:50%;background:var(--blue)}
.main-nav{display:flex;align-items:center;gap:28px;font-size:13px;font-weight:500}
.main-nav .active{color:var(--blue);border-bottom:2px solid var(--blue);padding-bottom:3px}
/* hero */
.hero{position:absolute;top:70px;left:0;width:1200px;height:610px;background:linear-gradient(90deg,#060708 0%,#14171b 45%,#2c2f33 100%)}
.hero-photo{position:absolute;right:0;top:0;width:620px;height:610px;background:linear-gradient(135deg,#4a5260,#2a2e35 55%,#7a6a4a)}
.hero-shade{position:absolute;left:0;top:0;width:760px;height:610px;background:linear-gradient(90deg,#060708 55%,rgba(6,7,8,0))}
.hero-copy{position:absolute;left:140px;top:200px;width:500px;color:#fff}
.hero-copy h1{font-size:25px;line-height:1.45;font-weight:600;margin-bottom:22px}
/* features */
.features{position:absolute;top:680px;left:0;width:1200px;height:200px;background:var(--light);display:flex;justify-content:center;gap:60px;padding-top:68px}
.feature{display:flex;gap:14px;width:260px}
.feature svg{flex:none}
.feature h3{font-size:12px;font-weight:600;line-height:1.3;text-transform:uppercase;margin-bottom:6px}
.feature p{font-size:11px;line-height:1.5}
/* about */
.about{position:absolute;top:880px;left:0;width:1200px;height:700px}
.about-frame{position:absolute;left:132px;top:70px;width:400px;height:430px;border:3px solid var(--blue)}
.about-photo{position:absolute;left:148px;top:56px;width:384px;height:410px;background:linear-gradient(160deg,#c9d1d8,#7c8894 60%,#3d4650)}
.about-copy{position:absolute;left:610px;top:70px;width:450px}
.eyebrow{color:var(--blue);font-size:14px;font-weight:500}
.about-copy h2{font-size:26px;font-weight:600;margin-bottom:14px}
.about-copy p{font-size:12px;margin-bottom:14px}
.stats{position:absolute;left:418px;top:530px;display:flex}
.stat{width:160px;height:95px;background:var(--blue);color:#fff;padding:22px 16px;border-right:1px solid rgba(255,255,255,.25)}
.stat.dark{background:#1a1c20}
.stat b{font-size:26px;font-weight:600;display:block;line-height:1}
.stat span{font-size:11px;line-height:1.3;display:block;margin-top:6px}
/* skills */
.skills{position:absolute;top:1600px;left:0;width:1200px;height:690px;background:var(--light);text-align:center}
.skills h2{font-size:30px;font-weight:600;margin-top:78px}
.rule{width:60px;height:3px;background:var(--blue);margin:10px auto 0}
.cards{display:flex;gap:20px;justify-content:center;margin-top:40px}
.card{width:292px;height:410px;position:relative;color:#fff}
.card-img{position:absolute;inset:0}
.card h3{position:absolute;bottom:22px;left:0;right:0;font-size:15px;font-weight:500}
.card.featured .card-img{background:#111}
.card.featured .card-body{position:absolute;top:170px;left:30px;right:30px}
.card.featured svg{margin-bottom:14px}
.card.featured h4{font-size:16px;font-weight:500;margin-bottom:8px}
.card.featured p{color:#bbb;font-size:11px}
.skills .btn{margin-top:30px}
/* vision */
.vision{position:absolute;top:2290px;left:0;width:1200px;height:550px}
.vm-box{position:absolute;left:160px;width:410px;height:180px;background:#fff;border:1px solid #e5e5e5;box-shadow:0 6px 20px rgba(0,0,0,.06);padding:28px 30px}
.vm-box h3{display:flex;align-items:center;gap:12px;font-size:22px;font-weight:600;margin-bottom:12px}
.vm-box p{font-size:11px}
.vm-frame{position:absolute;left:640px;top:90px;width:430px;height:380px;border:3px solid var(--blue)}
.vm-photo{position:absolute;left:618px;top:100px;width:434px;height:380px;background:linear-gradient(160deg,#2a2622,#6a4a24 50%,#c08a3c)}
/* clients */
.clients{position:absolute;top:2840px;left:0;width:1200px;height:400px;background:linear-gradient(180deg,#1a1410,#3b2614 60%,#241a12);text-align:center;color:#fff}
.clients h2{font-size:30px;font-weight:600;margin-top:68px}
.clients p.lead{color:#fff;font-size:14px;margin-top:10px}
.logo-row{display:flex;justify-content:center;gap:14px;margin-top:32px;align-items:center}
.logo-tile{width:168px;height:110px;background:#fff;display:flex;align-items:center;justify-content:center;gap:8px;font-size:22px;font-weight:600;color:var(--ink)}
.logo-tile i{width:16px;height:16px;background:var(--blue);display:block}
.arrow{width:38px;height:38px;border-radius:50%;background:#fff;display:flex;align-items:center;justify-content:center;margin:0 8px}
/* testimonials */
.reviews{position:absolute;top:3240px;left:0;width:1200px;height:400px;text-align:center}
.reviews h2{font-size:30px;font-weight:600;margin-top:78px}
.review-row{display:flex;justify-content:center;gap:40px;margin-top:44px;align-items:center}
.arrow.light{background:#fff;box-shadow:0 2px 8px rgba(0,0,0,.15)}
.review{width:450px;height:200px;background:#fff;box-shadow:0 6px 22px rgba(0,0,0,.08);border-bottom:3px solid var(--blue);padding:32px 60px;position:relative}
.review .quote{position:absolute;top:14px;left:0;right:0;font-size:80px;line-height:1;color:#eee;font-weight:700}
.review p{position:relative;font-size:11px}
.review h4{font-size:14px;font-weight:600;margin-top:10px}
.stars{color:var(--star);font-size:11px;letter-spacing:2px}
/* footer */
.site-footer{position:absolute;top:3640px;left:0;width:1200px;height:380px;background:var(--dark);color:#fff}
.footer-brand{position:absolute;left:140px;top:90px}
.footer-brand .brand{color:#fff}
.socials{display:flex;gap:10px;margin-top:24px;padding-left:50px}
.socials span{width:26px;height:26px;border:1px solid #fff;border-radius:50%;display:block}
.footer-col{position:absolute;top:80px}
.footer-col h4{font-size:15px;font-weight:500;margin-bottom:14px}
.footer-col li{list-style:none;font-size:12px;color:#ccc;margin-bottom:8px}
.footer-col li.on{color:#fff;text-decoration:underline}
.contact-item{display:flex;gap:12px;margin-bottom:14px;font-size:11px;color:#ccc;line-height:1.5}
.contact-item b{color:#fff;font-weight:500;display:block}
.contact-item svg{flex:none;margin-top:2px}
.footer-bottom{position:absolute;bottom:0;left:0;right:0;height:56px;border-top:1px solid #333;text-align:center;line-height:56px;font-size:11px;color:#bbb}
</style>
</head>
<body>

<header class="site-header">
  <div class="brand"><span class="brand-dot"></span>FEROLANZA</div>
  <nav class="main-nav">
    <span class="active">Maison</span><span>Compétences</span><span>Présentation</span><span class="btn">Contactez nous</span>
  </nav>
</header>

<section class="hero">
  <div class="hero-photo" role="img" aria-label="Deux ingénieurs en casque jaune consultant une tablette dans une usine"></div>
  <div class="hero-shade"></div>
  <div class="hero-copy">
    <h1>Ferolanza SA Est Une Entreprise De Construction Métallique Active Dans Les Domaines De La Tuyauterie Industrielle, De La Chaudronnerie Et De La Charpente Métallique.</h1>
    <span class="btn btn-white">Contactez nous</span>
  </div>
</section>

<section class="features">
  <div class="feature">
    <svg width="44" height="34" viewBox="0 0 44 34" fill="none" stroke="#1b1d22" stroke-width="1.6"><path d="M2 24h8l8-8h10l8 8h6"/><path d="M16 16l6 6 8-6"/></svg>
    <div><h3>Passion<br>for delivery</h3><p>Lorem ipsum dolor sit amet, consectetur adipiscing elit. Phasellus commodo</p></div>
  </div>
  <div class="feature">
    <svg width="44" height="34" viewBox="0 0 44 34" fill="none" stroke="#1b1d22" stroke-width="1.6"><path d="M2 24h8l8-8h10l8 8h6"/><path d="M16 16l6 6 8-6"/></svg>
    <div><h3>Passion<br>for people</h3><p>Lorem ipsum dolor sit amet, consectetur adipiscing elit. Phasellus commodo</p></div>
  </div>
  <div class="feature">
    <svg width="44" height="34" viewBox="0 0 44 34" fill="none" stroke="#1b1d22" stroke-width="1.6"><path d="M2 24h8l8-8h10l8 8h6"/><path d="M16 16l6 6 8-6"/></svg>
    <div><h3>Passion<br>for environment</h3><p>Lorem ipsum dolor sit amet, consectetur adipiscing elit. Phasellus commodo</p></div>
  </div>
</section>

<section class="about">
  <div class="about-frame"></div>
  <div class="about-photo" role="img" aria-label="Deux techniciens en casque jaune examinant une tablette"></div>
  <div class="about-copy">
    <div class="eyebrow">À Propos De Nous —</div>
    <h2>Ferolanza</h2>
    <p>Lorem ipsum dolor sit amet, consectetur adipiscing elit. Fusce efficitur libero non ante luctus tincidunt. Curabitur commodo tortor purus, sit amet pellentesque odio mattis vel. Suspendisse sit amet magna sed dui dapibus tristique.</p>
    <p>Fusce egestas purus imperdiet, consequat diam id, consequat nulla. Maecenas non felis pharetra, porta dolor nec, pulvinar dolor. Cras risus erat, iaculis vitae augue et, consequat luctus urna.</p>
    <p>Nullam eu sagittis urna, non rutrum tellus. Proin quis mi lectus. Curabitur id nulla non arcu auctor molestie. Nulla ipsum justo, pellentesque gravida bibendum nec, porta ac lectus. Phasellus ipsum justo, gravida nisl elementum id, dignissim at diam in hac habitasse platea dictumst.</p>
    <span class="btn">Contactez nous</span>
  </div>
  <div class="stats">
    <div class="stat dark"><b>150+</b><span>Projet Terminé</span></div>
    <div class="stat"><b>50+</b><span>Projet En Cours</span></div>
    <div class="stat dark"><b>45+</b><span>Équipe De Compétences</span></div>
    <div class="stat"><b>200+</b><span>Équipement Complémentaires</span></div>
  </div>
</section>

<section class="skills">
  <h2>Nos Compétences</h2>
  <div class="rule"></div>
  <div class="cards">
    <div class="card"><div class="card-img" role="img" aria-label="Installation de tuyauterie industrielle en acier inoxydable" style="background:linear-gradient(180deg,#b9c0c6,#6c757d 60%,#2b2f33)"></div><h3>Tuyauterie Industrielle</h3></div>
    <div class="card featured"><div class="card-img"></div>
      <div class="card-body">
        <svg width="44" height="44" viewBox="0 0 44 44" fill="none" stroke="#fff" stroke-width="1.6"><circle cx="22" cy="22" r="18"/><circle cx="22" cy="22" r="8"/></svg>
        <h4>Chaudronnerie</h4>
        <p>Lorem ipsum dolor sit amet, consectetur adipiscing elit. Fusce efficitur libero non ante luctus tincidunt. Curabitur commodo tortor purus, sit amet pellentesque odio mattis vel.</p>
      </div>
    </div>
    <div class="card"><div class="card-img" role="img" aria-label="Halle de charpente métallique éclairée" style="background:linear-gradient(180deg,#3a2a1a,#7a4e22 55%,#1e1812)"></div><h3>Charpente Métallique</h3></div>
  </div>
  <span class="btn">Contactez nous</span>
</section>

<section class="vision">
  <div class="vm-box" style="top:85px">
    <h3><svg width="30" height="30" viewBox="0 0 30 30" fill="none" stroke="#0054AA" stroke-width="1.6"><circle cx="15" cy="15" r="12"/><circle cx="15" cy="15" r="5"/></svg>Notre Vision</h3>
    <p>Aliquam in dignissim leo. Fusce tempus, metus nec hendrerit vehicula, lacus sapien ornare arcu, et consequat odio massa sed purus. Integer sagittis leo ac.</p>
  </div>
  <div class="vm-box" style="top:295px">
    <h3><svg width="30" height="30" viewBox="0 0 30 30" fill="none" stroke="#0054AA" stroke-width="1.6"><circle cx="15" cy="15" r="12"/><path d="M15 3v24M3 15h24"/></svg>Notre Mission</h3>
    <p>Aliquam in dignissim leo. Fusce tempus, metus nec hendrerit vehicula, lacus sapien ornare arcu, et consequat odio massa sed purus. Integer sagittis leo ac.</p>
  </div>
  <div class="vm-frame"></div>
  <div class="vm-photo" role="img" aria-label="Atelier métallurgique avec étincelles et métal en fusion"></div>
</section>

<section class="clients">
  <h2>Nos Clients</h2>
  <p class="lead">Aliquam in dignissim leo. Fusce tempus, metus nec hendrerit vehicula, lacus sapien ornare arcu.</p>
  <div class="logo-row">
    <span class="arrow"><svg width="14" height="14" viewBox="0 0 14 14" fill="none" stroke="#1b1d22" stroke-width="2"><path d="M9 2L4 7l5 5"/></svg></span>
    <div class="logo-tile"><i></i>Norvik</div>
    <div class="logo-tile"><i></i>Lumera</div>
    <div class="logo-tile"><i></i>Castra</div>
    <div class="logo-tile"><i></i>Oribel</div>
    <div class="logo-tile"><i></i>Zentho</div>
    <span class="arrow"><svg width="14" height="14" viewBox="0 0 14 14" fill="none" stroke="#1b1d22" stroke-width="2"><path d="M5 2l5 5-5 5"/></svg></span>
  </div>
</section>

<section class="reviews">
  <h2>Avis Clients Satisfaits</h2>
  <div class="review-row">
    <span class="arrow light"><svg width="14" height="14" viewBox="0 0 14 14" fill="none" stroke="#0054AA" stroke-width="2"><path d="M9 2L4 7l5 5"/></svg></span>
    <div class="review"><div class="quote">“</div>
      <p>Quisque mollis consequat efficitur. Vestibulum ante ipsum dui luctus et ultrices posuere cubilia curae; Donec vitae dapibus dolor. Sed laoreet pulvinar felis, ut euismod ante gravida eu, in rhoncus quam.</p>
      <h4>Clara Mendes</h4><div class="stars">★★★★★</div></div>
    <div class="review"><div class="quote">“</div>
      <p>Quisque mollis consequat efficitur. Vestibulum ante ipsum dui luctus et ultrices posuere cubilia curae; Donec vitae dapibus dolor. Sed laoreet pulvinar felis, ut euismod ante gravida eu, in rhoncus quam.</p>
      <h4>Victor Hale</h4><div class="stars">★★★★★</div></div>
    <span class="arrow light"><svg width="14" height="14" viewBox="0 0 14 14" fill="none" stroke="#0054AA" stroke-width="2"><path d="M5 2l5 5-5 5"/></svg></span>
  </div>
</section>

<footer class="site-footer">
  <div class="footer-brand">
    <div class="brand"><span class="brand-dot"></span>FEROLANZA</div>
    <div class="socials"><span></span><span></span><span></span></div>
  </div>
  <div class="footer-col" style="left:545px">
    <h4>Liens Rapides</h4>
    <ul><li class="on">Maison</li><li>Compétences</li><li>Présentation</li><li>Contactez nous</li></ul>
  </div>
  <div class="footer-col" style="left:830px">
    <h4>Détails Du Contact</h4>
    <div class="contact-item"><svg width="12" height="14" viewBox="0 0 12 14" fill="none" stroke="#fff" stroke-width="1.4"><path d="M6 13s5-5 5-8A5 5 0 0 0 1 5c0 3 5 8 5 8z"/><circle cx="6" cy="5" r="1.6"/></svg><span>12 Rue de l'Atelier,<br>1204 Genève, Suisse</span></div>
    <div class="contact-item"><svg width="12" height="12" viewBox="0 0 12 12" fill="none" stroke="#fff" stroke-width="1.4"><path d="M2 1h3l1 3-2 1a7 7 0 0 0 3 3l1-2 3 1v3c-6 0-9-3-9-9z"/></svg><span><b>Téléphone</b>+41 22 555 01 20</span></div>
    <div class="contact-item"><svg width="12" height="12" viewBox="0 0 12 12" fill="none" stroke="#fff" stroke-width="1.4"><rect x="1" y="2" width="10" height="8"/><path d="M1 2l5 4 5-4"/></svg><span><b>E-mail</b>info@ferolanza.example</span></div>
  </div>
  <div class="footer-bottom">© 2022 Ferolanza SA. Tous Droits Réservés</div>
</footer>

</body>
</html>
```